uk based ecommerce website requires fresh look ,high quality look and feel

we are a web based company selling eco friendly ground reinforcement grids to diy and construction sectors
our existing website is www.plumbrooksurfacing.co.uk ,

we have already updated the logo so that is the branding sorted .so we need a ecommerce website that is very much up-to date in design and layout and which has content management system for ease of use so that we can add products and information as required.

Use current logo as reference for colour scheme.
www.plumbrooksurfacing.co.uk

The current website has 6 pages accessible through the navigation bar, I would now like 5 pages, removing the need for the Trade Enquiries page possibly have it with along with contact us.
Updates

Target Market(s)

construction industry , diy end users,
retail market, landscapers, gardeners

Industry/Entity Type

Construction

Font styles to use
Other font styles liked:
• logo font prometo

Colors
f78f20
9bcb3c

Requirements
Must have
• logo colours and logo design in website with cms responsive design for tablet and mobile devices
• expect content to work flawlessly and look great across all devices
• HTML 5 custom design with coding as required
• must have good experiance in ecommerce website design
• eye catching, high quality look and feel and very user friedly ,very up-to date.
Nice to have
• picture slider show
• explain in writing what exactly i am getting in my ecommerce website
Should not have
• plain , basic design , old fashion looking ,cheap look

```html
<!DOCTYPE html>
<html lang="en">
<head>
<meta charset="utf-8">
<title>Plumbrook Surfacing – Ground Solutions</title>
<link href="https://fonts.googleapis.com/css2?family=Roboto:wght@400;500;700&display=swap" rel="stylesheet">
<style>
:root{
  --green:#8cc63f;
  --green-dark:#6da52a;
  --green-nav:#7dbb36;
  --orange:#f78f20;
  --dark:#222222;
  --darker:#1a1a1a;
  --ink:#111111;
  --muted:#c4c4c4;
  --white:#ffffff;
  --paper:#f2f2f2;
  --map:#f7dcb8;
  --map-light:#fbe8cf;
  --map-river:#f3b46a;
}
*{box-sizing:border-box;margin:0;padding:0}
html,body{width:1200px;height:3327px;overflow:hidden;background:var(--white)}
body{position:relative;font-family:'Roboto',Arial,sans-serif;color:var(--ink)}
.abs{position:absolute}
.btn{position:absolute;display:flex;align-items:center;justify-content:center;height:44px;border-radius:22px;background:var(--orange);color:var(--white);font-size:13px;font-weight:700;text-transform:uppercase;letter-spacing:.3px}
.btn--green{background:var(--green)}
.heading{position:absolute;font-size:30px;font-weight:700;text-transform:uppercase;color:var(--ink);letter-spacing:.3px;line-height:36px}
.heading::after{content:"";display:block;width:100%;height:3px;background:var(--green);margin-top:4px}
.copy{position:absolute;font-size:13px;line-height:16.5px;color:var(--muted)}
.copy p+p{margin-top:16px}
.photo{position:absolute;overflow:hidden}
.photo-frame{position:absolute;border:2px solid var(--white)}

/* header */
.site-header{position:absolute;left:0;top:0;width:1200px;height:137px}
.topbar{position:absolute;left:388px;top:0;right:0;height:40px;background:var(--darker)}
.topbar__phones{position:absolute;left:322px;top:11px;display:flex;gap:22px;color:var(--white);font-size:14px;font-weight:700}
.topbar__phones svg{margin-right:6px;vertical-align:-3px}
.socials{display:flex;gap:8px}
.socials span{width:20px;height:20px;border-radius:50%;background:var(--green);display:block}
.topbar .socials{position:absolute;left:590px;top:10px}
.topbar .socials span+span{background:#9a9a9a}
.navbar{position:absolute;left:360px;top:40px;right:0;height:97px;background:var(--green-nav);clip-path:polygon(28px 0,100% 0,100% 100%,0 100%)}
.navbar a{position:absolute;top:0;height:97px;display:flex;align-items:center;color:var(--white);font-size:13px;font-weight:500;text-decoration:none;text-transform:uppercase}
.navbar .is-active{background:var(--green-dark);padding:0 30px}
.brand{position:absolute;left:98px;top:24px;display:flex;align-items:center;gap:10px}
.brand__dot{width:72px;height:72px;background:var(--green);border-radius:50%}
.brand__name{font-size:30px;font-weight:700;color:var(--green-dark);line-height:1}
.brand__name small{display:block;font-size:15px;color:var(--ink);margin-top:4px;font-weight:700}

/* hero */
.hero{position:absolute;left:0;top:137px;width:1200px;height:462px;
  background:
    radial-gradient(ellipse 60% 45% at 78% 28%,rgba(120,90,60,.45),transparent 70%),
    radial-gradient(ellipse 70% 40% at 30% 85%,rgba(110,160,50,.55),transparent 70%),
    radial-gradient(ellipse 50% 40% at 85% 90%,rgba(70,110,40,.6),transparent 70%),
    linear-gradient(180deg,#2f3323 0%,#434a2a 35%,#4f6a27 70%,#6a8f33 100%)}
.hero__title{position:absolute;left:98px;top:117px;color:var(--white);font-size:46px;font-weight:700;line-height:52px;text-transform:uppercase}
.hero__text{position:absolute;left:98px;top:215px;color:var(--white);font-size:14px;line-height:17px}
.arrow{position:absolute;width:26px;height:46px}
.dots{position:absolute;display:flex;gap:15px}
.dots span{width:16px;height:16px;border-radius:50%;border:2px solid var(--green);display:block}
.dots .on{background:var(--green)}

/* product band */
.band{position:absolute;left:0;width:1200px;background:var(--dark)}
.card-title{position:absolute;width:312px;text-align:center;color:var(--white);font-size:20px;font-weight:700;text-transform:uppercase;line-height:24px}
.card-title::after{content:"";display:block;width:90px;height:3px;background:var(--green);margin:5px auto 0}
.card-text{position:absolute;width:300px;text-align:center;color:var(--white);font-size:13px;line-height:15.5px}

/* footer */
.footer{position:absolute;left:0;top:3034px;width:1200px;height:226px;background:var(--darker);color:var(--white)}
.footer h3{position:absolute;font-size:24px;font-weight:700;text-transform:uppercase;line-height:28px}
.footer h3::after{content:"";display:block;width:100%;height:3px;background:var(--green);margin-top:3px}
.quick-links{position:absolute;left:437px;top:75px;list-style:none;font-size:13px;font-weight:700;line-height:22px}
.newsletter-input{position:absolute;left:792px;top:107px;width:310px;height:34px;border-radius:17px;background:var(--white);font-size:12px;color:#999;padding:9px 18px}
.newsletter-input b{position:absolute;right:0;top:0;height:34px;width:110px;border-radius:17px;background:var(--orange);color:var(--white);font-size:11px;display:flex;align-items:center;justify-content:center}
.payments{position:absolute;left:0;top:3260px;width:1200px;height:67px;background:var(--paper);display:flex;justify-content:center;align-items:center;gap:12px}
.payments span{width:60px;height:34px;background:var(--white);border:1px solid #ccc;border-radius:3px;display:flex;align-items:center;justify-content:center;font-size:10px;font-weight:700;color:#444}
</style>
</head>
<body>

<header class="site-header">
  <div class="brand"><span class="brand__dot"></span><div class="brand__name">PLUMBROOK<small>SURFACING</small></div></div>
  <div class="topbar">
    <div class="topbar__phones">
      <span><svg width="18" height="14" viewBox="0 0 18 14"><path d="M1 5 Q9 -1 17 5 L15 7 L12 5 L12 3 Q9 2 6 3 L6 5 L3 7 Z M5 8 H13 L14 13 H4 Z" fill="#8cc63f"/></svg>0161-555-0148</span>
      <span>0800-555-0192</span>
    </div>
    <div class="socials"><span></span><span></span><span></span><span></span></div>
  </div>
  <nav class="navbar">
    <a class="is-active" style="left:72px">Home</a>
    <a style="left:204px">About Us</a>
    <a style="left:354px">Shop</a>
    <a style="left:438px">Downloads</a>
    <a style="left:587px">Contact Us</a>
    <svg class="abs" style="left:708px;top:34px" width="30" height="30" viewBox="0 0 30 30"><circle cx="12" cy="12" r="9" stroke="#fff" stroke-width="3" fill="none"/><path d="M19 19 L27 27" stroke="#fff" stroke-width="3.5" stroke-linecap="round"/></svg>
  </nav>
</header>

<section class="hero" role="img" aria-label="Photo of a decorative iron fence beside a grassy gravel driveway edge">
  <h1 class="hero__title">Gravel Stabilistion<br>for Driveways</h1>
  <p class="hero__text">Lorem Ipsum has been the industry's standard dummy text ever since the 1500s,<br>when an unknown printer took a galley of type and scrambled it to make a type specimen book.</p>
  <span class="btn" style="left:98px;top:267px;width:190px">Get a Quote</span>
  <svg class="arrow" style="left:40px;top:192px" viewBox="0 0 26 46"><path d="M22 3 L4 23 L22 43" stroke="#fff" stroke-width="5" fill="none"/></svg>
  <svg class="arrow" style="left:1134px;top:192px" viewBox="0 0 26 46"><path d="M4 3 L22 23 L4 43" stroke="#fff" stroke-width="5" fill="none"/></svg>
  <div class="dots" style="left:540px;top:421px"><span></span><span></span><span></span><span class="on"></span></div>
</section>

<section class="about">
  <h2 class="heading" style="left:98px;top:664px">Who We Are</h2>
  <div class="copy" style="left:98px;top:720px;width:570px">
    <p>Lorem Ipsum has been the industry's standard dummy text ever since the 1500s, when an unknown printer took a galley of type and scrambled it to make a type specimen book. It has survived not only five centuries, but also the leap into electronic typesetting, remaining essentially unchanged. It was popularised in the 1960s with the release of Letraset sheets containing Lorem Ipsum passages, and more recently with desktop publishing software like Aldus PageMaker including versions of Lorem Ipsum.</p>
    <p>Lorem Ipsum has been the industry's standard dummy text ever since the 1500s, when an unknown printer took a galley of type and scrambled it to make a type specimen book.</p>
  </div>
  <span class="btn" style="left:98px;top:890px;width:190px">Read More</span>
  <div class="photo" style="left:703px;top:672px;width:399px;height:262px;background:
    radial-gradient(ellipse 45% 30% at 35% 45%,rgba(40,90,80,.7),transparent 70%),
    radial-gradient(ellipse 40% 35% at 80% 72%,rgba(70,120,30,.8),transparent 70%),
    radial-gradient(ellipse 50% 25% at 50% 95%,rgba(120,150,50,.7),transparent 70%),
    linear-gradient(180deg,#5f8a2a 0%,#2b4617 40%,#3d6520 70%,#6f8d34 100%)" role="img" aria-label="Photo of a garden pavilion surrounded by trimmed hedges and lawn"></div>
  <div class="photo-frame" style="left:722px;top:688px;width:360px;height:230px"></div>
</section>

<section class="band" style="top:1007px;height:539px;background:radial-gradient(ellipse 70% 60% at 50% 40%,#2c2c2c,#1d1d1d)">
  <div class="photo" style="left:98px;top:71px;width:312px;height:286px;background:
    radial-gradient(ellipse 45% 20% at 70% 35%,rgba(180,140,90,.8),transparent 70%),
    linear-gradient(180deg,#dfe4e8 0%,#c7ccd0 22%,#8d7b5e 38%,#5a5550 60%,#3b3835 100%)" role="img" aria-label="Photo of a geotextile membrane laid on ground beside a timber fence"></div>
  <div class="photo" style="left:444px;top:71px;width:312px;height:286px;background:
    radial-gradient(ellipse 60% 25% at 50% 20%,rgba(140,140,140,.6),transparent 70%),
    radial-gradient(ellipse 60% 30% at 50% 80%,rgba(100,100,100,.5),transparent 70%),
    linear-gradient(180deg,#6e6e6e 0%,#444 45%,#5a5a5a 70%,#2e2e2e 100%)" role="img" aria-label="Photo of crushed stone in a hexagonal cell grid"></div>
  <div class="photo" style="left:790px;top:71px;width:312px;height:286px;background:
    radial-gradient(ellipse 60% 50% at 50% 45%,#f6a640,transparent 75%),
    linear-gradient(180deg,#f39a2a,#dc7a12)" role="img" aria-label="Photo of an orange heavy duty driveway grid panel"></div>
  <svg class="abs" style="left:915px;top:197px" width="62" height="36" viewBox="0 0 62 36"><path d="M2 18 Q31 -8 60 18 Q31 44 2 18 Z" fill="#fff"/><circle cx="31" cy="18" r="9" fill="#f39a2a"/></svg>
  <h3 class="card-title" style="left:98px;top:383px">Geotextile Membranes</h3>
  <h3 class="card-title" style="left:444px;top:383px">Light Domestic Driveways</h3>
  <h3 class="card-title" style="left:790px;top:383px">Heavy Domestic Driveways</h3>
  <p class="card-text" style="left:104px;top:427px">Lorem Ipsum has been the industry's standard dummy text ever since the 1500s, when an crambled it to make a type specimen book.</p>
  <p class="card-text" style="left:450px;top:427px">Lorem Ipsum has been the industry's standard dummy text ever since the 1500s, when an crambled it to make a type specimen book.</p>
  <p class="card-text" style="left:796px;top:427px">Lorem Ipsum has been the industry's standard dummy text ever since the 1500s, when an crambled it to make a type specimen book.</p>
  <svg class="arrow" style="left:40px;top:244px" viewBox="0 0 26 46"><path d="M22 3 L4 23 L22 43" stroke="#fff" stroke-width="5" fill="none"/></svg>
  <svg class="arrow" style="left:1134px;top:244px" viewBox="0 0 26 46"><path d="M4 3 L22 23 L4 43" stroke="#fff" stroke-width="5" fill="none"/></svg>
  <div class="dots" style="left:537px;top:497px"><span></span><span></span><span class="on"></span><span></span></div>
</section>

<section class="ground-solutions">
  <div class="photo" style="left:98px;top:1619px;width:490px;height:295px;background:
    radial-gradient(ellipse 30% 25% at 10% 70%,rgba(150,110,70,.7),transparent 70%),
    radial-gradient(ellipse 40% 18% at 70% 8%,rgba(160,150,140,.7),transparent 70%),
    linear-gradient(180deg,#9a958a 0%,#6c6860 18%,#2c2e33 38%,#24262b 70%,#1b1c20 100%)" role="img" aria-label="Photo of a black grid driveway in front of a brick house"></div>
  <div class="photo-frame" style="left:114px;top:1635px;width:458px;height:263px"></div>
  <h2 class="heading" style="right:98px;top:1612px">Ground Solutions</h2>
  <div class="copy" style="left:620px;top:1667px;width:482px;text-align:right">
    <p>Lorem Ipsum has been the industry's standard dummy text ever since the 1500s, when an unknown printer took a galley of type and scrambled it to make a type specimen book. It has survived not only five centuries, but also the leap into electronic typesetting, remaining essentially unchanged. It was popularised in the 1960s with the release of Letraset sheets containing Lorem Ipsum passages, and more recently with desktop publishing software like Aldus PageMaker including versions of Lorem Ipsum.</p>
    <p>Lorem Ipsum has been the industry's standard dummy text ever since the 1500s, when an unknown printer took a galley of type and scrambled it to make a type specimen book.</p>
  </div>
  <span class="btn" style="left:909px;top:1870px;width:193px">Read More</span>
  <div class="abs" style="left:98px;top:1953px;width:1022px;height:2px;background:#dddddd"></div>
</section>

<section class="grid-gravel">
  <h2 class="heading" style="left:98px;top:2000px">Grid Gravel</h2>
  <div class="copy" style="left:98px;top:2055px;width:470px">
    <p>Lorem Ipsum has been the industry's standard dummy text ever since the 1500s, when an unknown printer took a galley of type and scrambled it to make a type specimen book. It has survived not only five centuries, but also the leap into electronic typesetting, remaining essentially unchanged. It was popularised in the 1960s with the release of Letraset sheets containing Lorem Ipsum passages, and more recently with desktop publishing software like Aldus PageMaker including versions of Lorem Ipsum.</p>
    <p>Lorem Ipsum has been the industry's standard dummy text ever since the 1500s, when an unknown printer took a galley of type and scrambled it to make a type specimen book.</p>
  </div>
  <span class="btn" style="left:98px;top:2258px;width:190px">Read More</span>
  <div class="photo" style="left:659px;top:2007px;width:488px;height:295px;background:
    radial-gradient(ellipse 50% 20% at 60% 10%,rgba(190,175,150,.8),transparent 70%),
    radial-gradient(ellipse 30% 25% at 30% 75%,rgba(150,90,60,.5),transparent 70%),
    radial-gradient(ellipse 30% 25% at 75% 80%,rgba(150,90,60,.5),transparent 70%),
    linear-gradient(180deg,#a59986 0%,#5b4f43 35%,#3a302a 65%,#231f1c 100%)" role="img" aria-label="Close-up photo of gravel filling a hexagonal plastic cell grid"></div>
  <div class="photo-frame" style="left:675px;top:2022px;width:456px;height:265px"></div>
</section>

<section class="band" style="top:2393px;height:193px;background:radial-gradient(ellipse 60% 90% at 50% 40%,#333,#1b1b1b)">
  <h2 class="abs" style="left:0;width:1200px;top:18px;text-align:center;color:var(--white);font-size:30px;font-weight:500;text-transform:uppercase;line-height:36px">Gravel Grid Data Sheet</h2>
  <p class="abs" style="left:180px;width:840px;top:71px;text-align:center;color:var(--white);font-size:13px;line-height:17px">Lorem Ipsum has been the industry's standard dummy text ever since the 1500s, when an unknown printer took a galley of type and scrambled it to make a type specimen book. It has survived not only five centuries, but also the leap into electronic typesetting</p>
  <span class="btn btn--green" style="left:506px;top:122px;width:188px">Download Now!</span>
</section>

<section class="abs" style="left:0;top:2586px;width:1200px;height:448px;background:
  radial-gradient(ellipse 12% 70% at 4% 60%,rgba(243,180,106,.75),transparent 70%),
  radial-gradient(ellipse 40% 35% at 45% 40%,var(--map-light),transparent 70%),
  radial-gradient(ellipse 35% 30% at 82% 70%,var(--map-light),transparent 70%),
  linear-gradient(180deg,var(--map),#f5d3a9)" role="img" aria-label="Street map of the company location with a river and nearby businesses"></section>

<footer class="footer">
  <div class="abs" style="left:98px;top:40px;display:flex;align-items:center;gap:8px"><span style="width:40px;height:40px;border-radius:50%;background:var(--white);display:block"></span><span style="font-size:17px;font-weight:700;line-height:1">PLUMBROOK<br><span style="font-size:10px">SURFACING</span></span></div>
  <p class="abs" style="left:150px;top:92px;width:260px;font-size:12px;line-height:14px">Lorem Ipsum has been the industry's standard dummy text ever since the 1500s, when an unknown printer took a galley of it to make a type essentially unchanged.</p>
  <h3 style="left:437px;top:26px">Quick Links</h3>
  <ul class="quick-links"><li>HOME</li><li>ABOUT US</li><li>SHOP</li><li>DOWNLOADS</li><li>CONTACT US</li></ul>
  <h3 style="left:792px;top:26px">Newsletter</h3>
  <p class="abs" style="left:792px;top:78px;font-size:12px">Subscribe to our newsletter and join our 3 subscribers.</p>
  <div class="newsletter-input">you email<b>SUBSCRIBE</b></div>
  <div class="socials abs" style="left:792px;top:160px"><span></span><span style="background:#9a9a9a"></span><span style="background:#9a9a9a"></span><span style="background:#9a9a9a"></span></div>
</footer>

<div class="payments"><span>ZENPAY</span><span>KORA</span><span>TALLY</span><span>PAYLO</span><span>JUNO</span></div>

</body>
</html>
```